Scientific Conference A0 Poster

I need an A0 poster for a Emergency Medicine scientific conference designed urgently. Attached is the information needed/specification,
as well as a previous poster. Your creativity is much appreciated. Here is a link to how to create a poster (no doubt things you already know), there are also examples of other posters medical posters. I want mine to be the best.
https://www.vexlorstudy.co.uk/bripmed/how-to-make-a-poster/
Please keep the Holbury and Penwick Care Trust and PCS logos/graphics
Please can you find a way to graphically represent the visual elements listed in the specification as well as the statistics listed in the specification. The statistics should not just be quoted, they need to be graphically represented, if possible. I am comfortable with whatever you think works.
Doctors and Healthcare management
Healthcare

```html
<!DOCTYPE html>
<html lang="en">
<head>
<meta charset="utf-8">
<title>Crowding in Emergency Departments During COVID-19</title>
<link href="https://fonts.googleapis.com/css2?family=Arimo:wght@400;700&family=Bebas+Neue&family=Roboto+Condensed:wght@400;500;700&display=swap" rel="stylesheet">
<style>
:root{
  --blue:#0a6ebd;
  --ink:#1d1d1b;
  --panel:#f2f2f2;
  --panel2:#e9eaec;
  --dark:#231f20;
  --slate:#6f7f8d;
  --orange:#c8632a;
  --body:#2b2b2b;
}
*{box-sizing:border-box;margin:0;padding:0}
html,body{width:849px;height:1200px;overflow:hidden;background:#fff}
body{position:relative;font-family:Arimo,Arial,sans-serif;color:var(--body)}
.abs{position:absolute}
.title{left:36px;top:40px;font-family:Arimo,sans-serif;font-weight:700;font-size:39px;line-height:45px;letter-spacing:-1.2px;color:var(--ink)}
.title .hl{color:var(--blue)}
.subtitle{left:36px;top:190px;font-weight:700;font-size:17.5px;line-height:24px;color:var(--ink)}
.tag{background:var(--blue);color:#fff;padding:0 3px}
.brand{right:38px;top:58px;display:flex;align-items:center;gap:10px}
.brand-square{width:34px;height:34px;background:var(--blue)}
.brand-name{font-weight:700;font-size:17px;line-height:24px;color:var(--ink);text-align:right}
.panel{background:var(--panel)}
.h2{font-family:"Roboto Condensed",sans-serif;font-weight:700;color:var(--ink);font-size:21px;line-height:25px}
.bullets{list-style:none;font-size:9.4px;line-height:14.6px}
.bullets li{position:relative;padding-left:20px;margin-bottom:12px}
.bullets li::before{content:"";position:absolute;left:2px;top:2px;width:6px;height:6px;border-right:2.5px solid var(--blue);border-top:2.5px solid var(--blue);transform:rotate(45deg);margin-top:2px}
.band{background:var(--dark);color:#fff}
.bebas{font-family:"Bebas Neue",sans-serif;white-space:nowrap}
.node{position:absolute;border-radius:6px;font-family:"Roboto Condensed",sans-serif;text-align:center;font-size:9px;line-height:10.5px;display:flex;flex-direction:column;justify-content:center;align-items:center}
.n-slate{background:var(--slate);color:#fff;border:1.5px solid #3d4750}
.n-blue{background:var(--blue);color:#fff;border:1.5px solid #0b3f6b}
.n-white{background:#fff;color:var(--ink);border:1.5px solid var(--ink)}
.rec-h{font-family:"Roboto Condensed",sans-serif;font-weight:700;font-size:15.5px;line-height:17px;color:var(--ink)}
.rec-p{font-size:9.4px;line-height:13.6px}
.tech-h{font-weight:700;font-size:12px;color:var(--ink)}
.tech-p{font-size:9.4px;line-height:13.6px}
.refs{font-size:4.3px;line-height:6px;color:#ddd}
.refs p{margin-bottom:5px}
.vert{writing-mode:vertical-rl;transform:rotate(180deg);font-style:italic;white-space:nowrap}
</style>
</head>
<body>

<h1 class="abs title"><span class="hl">Crowding in</span> Emergency<br>Departments<br><span class="hl">During COVID-19</span></h1>
<svg class="abs" style="left:362px;top:123px" width="52" height="52" viewBox="0 0 52 52" aria-hidden="true">
  <g stroke="#1d1d1b" stroke-width="3" stroke-linecap="round">
    <line x1="26" y1="2" x2="26" y2="50"/><line x1="2" y1="26" x2="50" y2="26"/>
    <line x1="9" y1="9" x2="43" y2="43"/><line x1="43" y1="9" x2="9" y2="43"/>
  </g>
  <circle cx="26" cy="26" r="16" fill="#1d1d1b"/>
  <g fill="#fff"><circle cx="20" cy="20" r="2.5"/><circle cx="31" cy="19" r="2"/><circle cx="26" cy="28" r="3"/><circle cx="18" cy="31" r="2"/><circle cx="33" cy="31" r="2.5"/></g>
</svg>

<p class="abs subtitle">A Critical Review of existing and novel measures<br>adopted by global health institutions <span class="tag">Dr Tomi Arden,</span><br><span class="tag">Emergency Medicine Consultant</span></p>

<div class="abs brand">
  <div class="brand-square"></div>
  <div class="brand-name">Holbury and Penwick<br>Care Trust</div>
</div>

<!-- Introduction -->
<section class="abs panel" style="left:30px;top:276px;width:258px;height:424px">
  <h2 class="h2" style="text-align:center;margin-top:20px">Introduction &amp;<br>Background</h2>
  <ul class="bullets" style="margin:22px 34px 0 20px">
    <li>Emergency departments (ED) experienced unprecedented crowding during the COVID-1 pandemic.</li>
    <li>Hospitals faced increased healthcare demand, leading to overflows in intensive care units and emergency care, with limited hospital bed availability.</li>
  </ul>
  <svg class="abs" style="left:10px;top:235px" width="240" height="180" viewBox="0 0 240 180" role="img" aria-label="Line chart of daily new hospital admissions for COVID-19">
    <text x="2" y="10" font-family="Times New Roman,serif" font-weight="700" font-size="6.5" fill="#333">UK: Daily new hospital admissions for COVID-19</text>
    <text x="2" y="17" font-size="3.3" fill="#555">Hospital data available per nation; figures not fully comparable across regions.</text>
    <rect x="222" y="3" width="16" height="10" fill="#1f3b6e"/>
    <g stroke="#ccc" stroke-width=".4" stroke-dasharray="1.5 1.5">
      <line x1="18" y1="44" x2="225" y2="44"/><line x1="18" y1="59" x2="225" y2="59"/><line x1="18" y1="74" x2="225" y2="74"/><line x1="18" y1="89" x2="225" y2="89"/><line x1="18" y1="104" x2="225" y2="104"/><line x1="18" y1="119" x2="225" y2="119"/><line x1="18" y1="134" x2="225" y2="134"/>
    </g>
    <g font-size="3.3" fill="#555" text-anchor="end">
      <text x="15" y="46">3,500</text><text x="15" y="61">3,000</text><text x="15" y="76">2,500</text><text x="15" y="91">2,000</text><text x="15" y="106">1,500</text><text x="15" y="121">1,000</text><text x="15" y="136">500</text><text x="15" y="151">0</text>
    </g>
    <line x1="18" y1="149" x2="225" y2="149" stroke="#888" stroke-width=".5"/>
    <polyline fill="none" stroke="#c8632a" stroke-width=".8" points="20,64 24,100 28,125 32,140 36,146 42,147 48,145 52,132 56,108 60,118 64,112 68,96 70,70 72,42 74,60 77,105 80,132 84,142 90,144 96,146 102,145 106,135 108,124 111,130 114,120 117,128 120,118 123,126 126,113 129,128 132,96 134,104 136,120 140,112 143,92 146,108 150,135 154,128 157,98 160,110 163,130 166,118 169,108 172,132 175,124 178,110 181,134 184,118 187,112 190,126 194,136 198,144 203,146 207,138 210,140 213,132 216,138 220,140"/>
    <text x="222" y="142" font-size="3" fill="#c8632a">England</text>
    <g font-size="3" fill="#555">
      <text x="26" y="156">Mar 25, 2020</text><text x="64" y="156">Feb 24, 2021</text><text x="100" y="156">Sep 12, 2021</text><text x="132" y="156">Mar 31, 2022</text><text x="160" y="156">Oct 17, 2022</text><text x="202" y="156">Dec 8, 2023</text>
      <text x="2" y="168" font-weight="700">Data source: Government statistics (2024)</text>
      <text x="238" y="168" text-anchor="end">DataAtlas.org | CC BY</text>
    </g>
  </svg>
</section>

<!-- Impact -->
<section class="abs panel" style="left:296px;top:276px;width:259px;height:424px">
  <h2 class="h2" style="text-align:center;margin-top:20px">The Impact of ED<br>Crowding During COVID-19</h2>
  <ul class="bullets" style="margin:22px 18px 0 18px">
    <li>Overcrowding peaked during the pandemic, with a 28% increase following the removal of COVID-19 lockdowns. (Halvern et al., 2020)</li>
    <li>This led to high-risk environments for both patients and staff, resulting in medical errors, prolonged hospital stays, and increased in-hospital mortality.</li>
  </ul>
  <div class="abs" style="left:18px;top:218px;font-weight:700;font-size:19.5px;color:var(--blue)">Another bout of excess</div>
  <div class="abs" style="left:20px;top:255px;font-weight:700;font-size:8.6px;line-height:11px;color:var(--ink)">England and wales, number of deaths*<br>compared with 2016-19 average</div>
  <svg class="abs" style="left:14px;top:282px" width="240" height="140" viewBox="0 0 240 140" role="img" aria-label="Line chart of excess deaths compared with the 2016-19 average">
    <g stroke="#999" stroke-width=".5">
      <line x1="2" y1="4" x2="200" y2="4"/><line x1="2" y1="19.5" x2="200" y2="19.5"/><line x1="2" y1="35" x2="200" y2="35"/><line x1="2" y1="50.5" x2="200" y2="50.5"/><line x1="2" y1="66" x2="200" y2="66"/><line x1="2" y1="81.5" x2="200" y2="81.5" stroke="#333"/><line x1="2" y1="97" x2="200" y2="97"/>
    </g>
    <g font-size="8" font-weight="700" fill="#222" text-anchor="end">
      <text x="229" y="7">10,000</text><text x="229" y="22.5">8,000</text><text x="229" y="38">6,000</text><text x="229" y="53.5">4,000</text><text x="229" y="69">2,000</text><text x="229" y="84.5">0</text><text x="229" y="100">-2,000</text>
    </g>
    <polyline fill="none" stroke="#0a6ebd" stroke-width="1.6" points="2,90 5,84 8,91 11,82 15,86 19,82 23,88 27,83 31,85 35,80 39,86 43,84 47,80 51,83 54,76 57,82 61,84 65,85 69,83 73,86 77,84 81,88 85,84 89,83 93,80 96,86 100,88 104,85 107,50 109,6 111,60 113,85 117,90 121,82 125,78 128,84 131,55 133,40 135,70 138,88 142,88 145,80 147,72 150,72 154,74 158,70 161,80 164,72 167,76 170,70 173,74 176,68 179,70 182,66"/>
    <g font-size="8.3" font-weight="700" fill="#222">
      <text x="8" y="116">2016</text><text x="39" y="116">17</text><text x="66" y="116">18</text><text x="92" y="116">19</text><text x="118" y="116">20</text><text x="145" y="116">21</text><text x="171" y="116">22</text>
    </g>
    <g font-size="6.2" font-weight="700" fill="#333">
      <text x="4" y="131">Sources: NSO: The Ledger</text><text x="236" y="131" text-anchor="end">*Four-week moving average</text>
    </g>
  </svg>
</section>

<!-- Addressing -->
<section class="abs panel" style="left:561px;top:276px;width:259px;height:424px">
  <h2 class="h2" style="font-size:24px;margin:16px 0 0 12px">Addressing ED Crowding</h2>
  <svg class="abs" style="left:0;top:0" width="259" height="424" aria-hidden="true">
    <g fill="none" stroke="#333" stroke-width="1.3">
      <path d="M128 100 V120 M72 136 V122 H183 V136"/>
      <path d="M128 216 V236 M53 252 V236 H201 V252 M128 236 V252"/>
      <path d="M128 335 V354 M70 367 V354 H189 V367"/>
    </g>
  </svg>
  <div class="node n-slate" style="left:66px;top:76px;width:123px;height:25px;font-size:10.5px;font-weight:700">Hospital Transformations</div>
  <div class="node n-slate" style="left:31px;top:136px;width:90px;height:29px">Dedicated COVID-19<br>treatment zones</div>
  <div class="node n-slate" style="left:140px;top:136px;width:90px;height:29px">Expanding<br>telehealth services</div>
  <div class="node n-blue" style="left:66px;top:190px;width:123px;height:27px;font-size:10.5px;font-weight:700;line-height:10px">Process Optimisation<span style="font-size:7px;font-weight:400">to improve patient flow</span></div>
  <div class="node n-blue" style="left:31px;top:252px;width:55px;height:29px">Fast-track<br>Pathways</div>
  <div class="node n-blue" style="left:100px;top:252px;width:55px;height:29px">Improved<br>Triage</div>
  <div class="node n-blue" style="left:173px;top:252px;width:56px;height:29px">Discharge<br>Planning</div>
  <div class="node n-white" style="left:66px;top:309px;width:123px;height:26px;font-size:10.5px;font-weight:700">Leadership &amp; Training</div>
  <div class="node n-white" style="left:16px;top:365px;width:100px;height:41px">Enhanced adaptibility<br>through evidence based<br>training programs</div>
  <div class="node n-white" style="left:139px;top:365px;width:102px;height:41px">Efficient ED<br>management during<br>surges</div>
</section>

<!-- Stat bands -->
<div class="abs band" style="left:30px;top:700px;width:258px;height:86px">
  <div class="abs bebas" style="left:6px;top:6px;font-size:74px;line-height:74px;color:var(--blue)">157</div>
  <div class="abs bebas" style="left:84px;top:12px;font-size:22px;line-height:20px">Average</div>
  <div class="abs bebas" style="left:82px;top:34px;font-size:13px;line-height:15px">Daily admissions<br>during <span style="color:var(--blue)">COVID-19</span></div>
  <div class="abs" style="left:164px;top:14px;width:1px;height:58px;background:#fff"></div>
  <div class="abs bebas" style="left:172px;top:14px;font-size:17px;line-height:18px">ED spening</div>
  <div class="abs bebas" style="left:172px;top:32px;font-size:23px;line-height:22px;color:var(--blue)">152 days</div>
  <div class="abs bebas" style="left:172px;top:55px;font-size:12px">in overcrowding</div>
</div>

<div class="abs band" style="left:296px;top:700px;width:259px;height:86px">
  <svg class="abs" style="left:6px;top:18px" width="52" height="48" viewBox="0 0 52 48" aria-hidden="true">
    <path d="M4 6 H48 L26 44 Z" fill="none" stroke="#fff" stroke-width="3.5" stroke-linejoin="round"/>
    <line x1="26" y1="14" x2="26" y2="28" stroke="var(--blue)" stroke-width="3.5"/><circle cx="26" cy="34" r="2.2" fill="var(--blue)"/>
  </svg>
  <div class="abs bebas" style="left:66px;top:6px;font-size:80px;line-height:80px;color:var(--blue)">25</div>
  <div class="abs bebas" style="left:114px;top:46px;font-size:32px;line-height:32px">%</div>
  <div class="abs bebas" style="left:145px;top:14px;font-size:17px;line-height:17px;color:var(--blue)">Urgent hospital</div>
  <div class="abs bebas" style="left:145px;top:31px;font-size:28px;line-height:26px">Admission</div>
  <div class="abs bebas" style="left:145px;top:60px;font-size:12px">during the pandemic</div>
  <div class="abs vert" style="left:243px;top:8px;font-size:6.5px;width:9px;height:72px;text-align:center">(Corvadi et al., 2020)</div>
</div>

<div class="abs band" style="left:561px;top:700px;width:259px;height:86px">
  <svg class="abs" style="left:8px;top:8px" width="36" height="60" viewBox="0 0 36 60" aria-hidden="true">
    <path d="M10 58 V8 M3 16 L10 4 L17 16" fill="none" stroke="var(--blue)" stroke-width="3"/>
    <path d="M10 48 L30 32 M22 31 L31 31 L29 40" fill="none" stroke="var(--blue)" stroke-width="3"/>
  </svg>
  <div class="abs" style="left:52px;top:12px;font-size:6.5px;line-height:8px">Each hour of ambulance<br>diversion is associated with</div>
  <div class="abs bebas" style="left:51px;top:28px;font-size:30px;line-height:30px">$1,086/HR</div>
  <div class="abs" style="left:52px;top:58px;font-size:5.8px">deducted from hospital revenue</div>
  <div class="abs" role="img" aria-label="Ambulance icon" style="left:174px;top:12px;width:62px;height:46px;border-radius:8px;background:var(--blue)"></div>
  <div class="abs vert" style="left:243px;top:2px;font-size:6.5px;width:9px;height:72px;text-align:center">(Brantley et al., 2020)</div>
  <div class="abs" style="left:2px;top:74px;width:255px;border-top:.6px solid #fff;font-size:6.8px;text-align:center;padding-top:2px;white-space:nowrap">Reducing ambulance diversion could save hospitals around $9,000 annually</div>
</div>

<!-- Technology -->
<section class="abs panel" style="left:30px;top:792px;width:258px;height:306px">
  <h2 class="h2" style="font-size:20px;line-height:24px;margin:12px 0 0 15px">Technological Solutions<br>for Managing ED Crowding</h2>
  <svg class="abs" style="left:16px;top:74px" width="60" height="60" viewBox="0 0 60 60" aria-hidden="true">
    <circle cx="36" cy="22" r="18" fill="none" stroke="var(--blue)" stroke-width="2"/>
    <path d="M30 17 H44 M40 13 L44 17 L40 21 M42 27 H28 M32 23 L28 27 L32 31" fill="none" stroke="var(--blue)" stroke-width="2"/>
    <path d="M6 30 C2 40 14 56 26 56 L30 50 L22 44 L18 48 C14 46 10 40 10 36 L14 32 L10 24 Z" fill="none" stroke="var(--blue)" stroke-width="2" stroke-linejoin="round"/>
  </svg>
  <div class="abs tech-h" style="left:95px;top:76px">Telemedicine</div>
  <p class="abs tech-p" style="left:95px;top:92px;width:160px">Remote delivery of healthcare services using telecommunication technologies.</p>
  <div class="abs tech-h" style="left:24px;top:153px">Internet Hospitals</div>
  <p class="abs tech-p" style="left:24px;top:169px;width:150px">Implementation of multi-centre internet hospitals to reduce physical ED visits and crowding.</p>
  <svg class="abs" style="left:190px;top:142px" width="42" height="70" viewBox="0 0 42 70" aria-hidden="true">
    <path d="M6 12 A20 20 0 0 1 36 12 M11 17 A13 13 0 0 1 31 17" fill="none" stroke="var(--blue)" stroke-width="2"/>
    <circle cx="21" cy="22" r="3" fill="none" stroke="var(--blue)" stroke-width="2"/>
    <rect x="6" y="32" width="30" height="36" fill="none" stroke="var(--blue)" stroke-width="2"/>
    <path d="M6 40 H36 M21 46 V58 M15 52 H27" stroke="var(--blue)" stroke-width="2"/>
  </svg>
  <div class="abs" role="img" aria-label="Brain circuit icon for AI" style="left:20px;top:234px;width:56px;height:56px;border-radius:50%;border:2px solid var(--blue)"></div>
  <div class="abs tech-h" style="left:95px;top:231px">AI Advancements</div>
  <p class="abs tech-p" style="left:95px;top:247px;width:150px">AI-enabled tools like virtual waiting rooms and online symptom checkers streamlined patient management.</p>
</section>

<div class="abs band" style="left:30px;top:1098px;width:258px;height:78px">
  <div class="abs bebas" style="left:14px;top:8px;font-size:52px;line-height:52px">1 Billion</div>
  <div class="abs" style="left:18px;top:60px;font-size:6.8px;font-style:italic">telehealth visits globally by the end of 2021</div>
  <div class="abs" role="img" aria-label="Globe icon" style="left:175px;top:10px;width:56px;height:56px;border-radius:50%;background:var(--blue)"></div>
  <div class="abs vert" style="left:243px;top:6px;font-size:6.5px;width:9px;height:66px;text-align:center">(Tarn et al., 2021)</div>
</div>

<!-- Recommendations -->
<section class="abs" style="left:296px;top:792px;width:524px;height:274px;background:var(--panel2)">
  <h2 class="h2" style="font-size:20px;line-height:25px;margin:14px 0 0 24px">Recommendations for<br>Future Crowding Management</h2>
  <svg class="abs" style="left:453px;top:16px" width="48" height="48" viewBox="0 0 48 48" aria-hidden="true">
    <circle cx="24" cy="24" r="21" fill="none" stroke="var(--blue)" stroke-width="3.5"/>
    <path d="M14 25 L21 32 L35 17" fill="none" stroke="var(--blue)" stroke-width="4"/>
  </svg>
  <div class="abs rec-h" style="left:24px;top:78px">Data-driven Real<br>-Time Bottleneck<br>removal</div>
  <div class="abs rec-h" style="left:198px;top:78px">Empowered<br>Interdepartmental<br>Collaboration</div>
  <div class="abs rec-h" style="left:373px;top:78px">Proactive<br>Community<br>Care</div>
  <div class="abs" style="left:24px;top:150px;width:470px;height:1.6px;background:var(--ink)"></div>
  <div class="abs" style="left:20px;top:145px;width:11px;height:11px;border-radius:50%;background:var(--blue)"></div>
  <div class="abs" style="left:196px;top:145px;width:11px;height:11px;border-radius:50%;background:var(--blue)"></div>
  <div class="abs" style="left:369px;top:145px;width:11px;height:11px;border-radius:50%;background:var(--blue)"></div>
  <p class="abs rec-p" style="left:25px;top:172px;width:115px">Live dashboards pinpoint resource constraints (imaging, labs, beds) and patient acuity for dynamic resource allocation and on-the-fly interventions.</p>
  <p class="abs rec-p" style="left:198px;top:172px;width:140px">Interdepartmental visibility and shared ownership of patient flow. Multidisciplinary patient flow teams. Inpatient units proactively prepare for admissions, optimising bed availability.</p>
  <p class="abs rec-p" style="left:372px;top:172px;width:130px">Leveraging telehealth and community partnerships for remote monitoring, virtual urgent care, and preventative care to reduce ED demand.</p>
</section>

<!-- References -->
<section class="abs band" style="left:296px;top:1072px;width:524px;height:104px">
  <div class="abs vert" style="left:4px;top:6px;height:94px;font-family:'Roboto Condensed',sans-serif;font-weight:700;font-style:normal;font-size:17px">References</div>
  <div class="abs refs" style="left:30px;top:8px;width:245px">
    <p>Halden, R. et al. (2020). Emergency department crowding and hospital transformation during a pandemic. Journal of Acute Care, 28(1), 1-10.</p>
    <p>Norvik, J. et al. (2021). Emergency department overcrowding during an outbreak: a letter. Archives of Urgent Medicine, 9(1).</p>
    <p>Pellow, A. et al. (2021). International report on department crowding and access block. Urgent Care Journal, 38(3), 245-246.</p>
    <p>Carrow, J. et al. (2020). Factors affecting emergency department crowding. Urgent Care Clinics, 38(3), 573-587.</p>
  </div>
  <div class="abs refs" style="left:290px;top:8px;width:226px">
    <p>Tarn, M. et al. (2021). Impact of a pandemic on department attendance and visit characteristics.</p>
    <p>Corvadi, F. et al. (2020). The changing patient flow in a trauma center emergency department.</p>
    <p>Halvern, L. et al. (2020). Early lessons that may reduce future department crowding. Urgent Care Australasia, 32(6), 1077-1079.</p>
    <p>Data Atlas (2023). Number of patients newly admitted to hospitals in a given week. Accessed 1/10/24.</p>
  </div>
</section>

</body>
</html>
```